Software company seeking fresh website design

Using an already existing logo create a fresh, clean and professional web design for our company "Nimbra Works". Nimbra Works focuses on making business better through system integrations and software product development.

We're looking for a web design which has layouts for the following pages:
- Home Page
- Team Page
- Case Studies
- Market (List of Products)
- Product Page (Individual Product Details)
- About Page
- Media Page

Some websites and designs we'd like you to take inspiration from:
- Quarnel.com
- https://www.plorvate.net/gallery/71830264/Vantrel-redesign
- https://zimmerpost.com/shots/5918304-Bright-Frames-Website-Design-for-a-Software-Company

Ideally the design should communicate an enterprise-level business with years of experience that can be trusted to deliver on budget and on-time.

Target Market(s)

Medium to High-Level Enterprise

Industry/Entity Type

Software Development

Coding

Coded - Design and coding required

Number of Pages Required

5+ page

Font styles to use
Sans Serif

Colors

Designer to choose colors to be used in the design.

Requirements
Must have
• - High Level of Professionalism
• - Be a unique design
• - Come with well-formatted and organised html + css + javascript
• - Must work on ie9, latest Chrome, latest Firefox, latest safari. iPhone6 and Android
• - Must be a progressive template
• - Must incorporate logo colors or at least be compatible with them
Nice to have
• - Hero, an area to display things we're proud of but look good without that area if need be.
• - Juicy animations that are performant and degrade nicely
Should not have
• - Submission must not be a template re-branded for the business

```html
<!DOCTYPE html>
<html lang="en">
<head>
<meta charset="utf-8">
<title>Nimbra Works — Home</title>
<link href="https://fonts.googleapis.com/css2?family=Montserrat:wght@400;500;600;700&display=swap" rel="stylesheet">
<style>
:root{
  --orange:#ec5a1f;
  --orange-deep:#d9460f;
  --ink:#2b2b2b;
  --text:#3a3a3a;
  --muted:#6b6b6b;
  --white:#ffffff;
  --footer-bg:#f3efed;
  --line:#d8d2cf;
  --black:#111111;
  --sky:#29b6e6;
  --navy:#1f2733;
}
*{margin:0;padding:0;box-sizing:border-box}
html,body{width:1200px;height:3191px;overflow:hidden}
body{position:relative;background:var(--white);font-family:'Montserrat',sans-serif;color:var(--text)}
.abs{position:absolute}

/* hero */
.hero-band{left:0;top:0;width:1200px;height:660px}
.brand{left:85px;top:38px;display:flex;align-items:center;gap:10px;color:var(--white);font-weight:700;font-size:22px}
.brand-mark{width:22px;height:22px;background:var(--white)}
.nav{top:44px;left:0;width:1200px}
.nav a{position:absolute;color:var(--white);text-decoration:none;font-size:15px;font-weight:500}
.device{border-radius:34px;background:#e9ecef;box-shadow:0 20px 40px rgba(0,0,0,.25);padding:22px}
.device-screen{width:100%;height:100%;border-radius:10px;background:linear-gradient(135deg,#2a3340 0%,#3d4a5a 45%,#e8eef2 46%,#f4f7f9 100%)}

/* sections */
.eyebrow{font-size:23px;color:var(--ink);font-weight:500}
.headline{font-size:56px;color:var(--ink);font-weight:500;line-height:1.1}
.headline strong{color:var(--orange);font-weight:700}
.body-copy{font-size:14.5px;line-height:22px;color:var(--text)}
.btn{display:flex;align-items:center;justify-content:center;border-radius:22px;font-size:13px;font-weight:600;color:var(--white);background:var(--orange);box-shadow:0 4px 10px rgba(236,90,31,.35)}
.center{text-align:center}

.photo{border-radius:28px;box-shadow:0 20px 40px rgba(0,0,0,.25)}

/* news */
.news-card{background:var(--white);box-shadow:0 3px 18px rgba(0,0,0,.14);padding:36px 32px}
.news-date{font-size:12.5px;color:var(--ink);font-weight:500}
.news-title{font-size:21px;line-height:28px;color:var(--ink);font-weight:500;margin-top:22px}
.news-text{font-size:13px;line-height:19px;color:var(--text);margin-top:14px}
.news-more{font-size:13px;color:var(--orange);margin-top:22px;font-weight:500}

/* cta */
.cta-kicker{font-size:22px;color:var(--orange);font-weight:500}
.cta-line{font-size:29px;color:var(--ink);font-weight:500}
.btn-dark{background:var(--black);box-shadow:0 4px 10px rgba(0,0,0,.3)}

/* footer */
.footer{left:0;top:2877px;width:1200px;height:314px;background:var(--footer-bg)}
.footer-brand{left:85px;top:3030px;display:flex;align-items:center;gap:12px;color:var(--ink);font-weight:700;font-size:36px}
.footer-brand .brand-mark{width:30px;height:30px;background:var(--orange)}
.v-rule{width:1px;background:var(--line)}
.footer-heading{font-size:17px;color:var(--ink);font-weight:500}
.contact-row{display:flex;gap:22px;align-items:flex-start;font-size:13px;color:var(--text)}
.contact-row svg{flex:none;margin-top:2px}
.contact-name{font-size:16px;font-weight:600;color:var(--ink);display:block;margin-bottom:6px}
.newsletter{display:flex}
.newsletter-input{width:164px;height:43px;border:1px solid #c9c2bf;background:var(--white);font-size:12px;color:#9a9a9a;display:flex;align-items:center;justify-content:center}
.newsletter-submit{width:104px;height:43px;background:var(--orange);color:var(--white);font-size:16px;font-weight:700;display:flex;align-items:center;justify-content:center}
.social{display:flex;gap:9px}
.social span{width:30px;height:30px;border-radius:50%}
.h-rule{left:89px;top:3122px;width:1032px;height:1px;background:var(--line)}
.footer-nav{left:89px;top:3142px;font-size:12.5px;color:var(--text)}
.footer-nav span{margin:0 10px;color:#999}
.copyright{right:79px;top:3142px;font-size:12.5px;color:var(--text)}
</style>
</head>
<body>

<!-- Hero -->
<svg class="abs hero-band" viewBox="0 0 1200 660" aria-hidden="true">
  <defs>
    <linearGradient id="heroFill" x1="0" y1="0" x2="1" y2="1">
      <stop offset="0" stop-color="#f06a2a"/>
      <stop offset="1" stop-color="#e4480f"/>
    </linearGradient>
  </defs>
  <polygon points="0,0 1200,0 1200,110 0,640" fill="url(#heroFill)"/>
</svg>

<div class="abs brand"><span class="brand-mark"></span>Nimbra Works</div>

<nav class="abs nav">
  <a style="left:500px">Home</a>
  <a style="left:577px">Who We Are</a>
  <a style="left:702px">What We Do</a>
  <a style="left:828px">Case Study</a>
  <a style="left:945px">Blog</a>
  <a style="left:1036px">Contact Us</a>
</nav>

<div class="abs device" style="left:535px;top:265px;width:450px;height:340px;transform:rotate(-8deg)">
  <div class="device-screen" role="img" aria-label="Tablet showing an analytics dashboard"></div>
</div>
<div class="abs device" style="left:1000px;top:140px;width:260px;height:470px;transform:rotate(-8deg)">
  <div class="device-screen" role="img" aria-label="Second tablet showing a dashboard screen"></div>
</div>

<!-- Welcome -->
<div class="abs center" style="left:0;top:738px;width:1200px">
  <p class="eyebrow">Welcome to</p>
  <h1 class="headline" style="margin-top:8px"><strong>Nimbra</strong> Works</h1>
</div>
<p class="abs body-copy center" style="left:196px;top:848px;width:812px">Contrary to popular belief, Lorem Ipsum is not simply random text. It has roots in a piece of classical Latin literature from 45 BC, making it over 2000 years old. Tomas Ardelle, a Latin professor at Corvane College in Virginia, looked up one of the more obscure Latin words, consectetur, from a Lorem Ipsum passage, and going through the cites of the word in classical literature, discovered the undoubtable source. Lorem Ipsum comes from sections 1.10.32 and 1.10.33 of "de Finibus Bonorum et Malorum" (The Extremes of Good and Evil) by Varelius, written in 45 BC. This book is a treatise on the theory of ethics, very popular during the Renaissance.</p>
<div class="abs btn" style="left:525px;top:1013px;width:147px;height:42px">Read More</div>

<!-- System Integrations -->
<p class="abs eyebrow" style="left:89px;top:1178px">We focuses on</p>
<h2 class="abs headline" style="left:87px;top:1215px"><strong>System</strong> Integrations</h2>
<p class="abs body-copy" style="left:89px;top:1303px;width:590px">Sed ut perspiciatis unde omnis iste natus error sit voluptatem accusantium doloremque laudantium, totam rem aperiam, eaque ipsa quae ab illo inventore veritatis et quasi architecto beatae vitae dicta sunt explicabo. Nemo enim ipsam voluptatem quia voluptas sit aspernatur aut odit aut fugit, sed quia consequuntur magni dolores eos qui ratione voluptatem sequi nesciunt. Neque porro quisquam est, qui dolorem ipsum quia dolor sit amet, consectetur, adipisci velit, sed quia non numquam eius modi tempora incidunt ut labore et dolore magnam aliquam quaerat voluptatem.</p>
<div class="abs btn" style="left:89px;top:1490px;width:147px;height:42px">Read More</div>

<div class="abs photo" role="img" aria-label="Dark card with a glowing integration illustration" style="left:725px;top:1245px;width:265px;height:325px;background:linear-gradient(160deg,#2a303a,#1a1f27);transform:rotate(-8deg)"></div>
<div class="abs photo" role="img" aria-label="Photo of hands holding a phone on a blue desk with keyboard and notebook" style="left:985px;top:1215px;width:260px;height:370px;background:linear-gradient(160deg,#e9f3f8 0%,#5cc4ec 45%,#2aa7dd 100%);transform:rotate(-8deg)"></div>

<!-- Software Development -->
<div class="abs photo" role="img" aria-label="Dark card with red isometric cubes" style="left:-70px;top:1680px;width:230px;height:385px;background:linear-gradient(160deg,#2b3a4c,#1b2633);transform:rotate(-8deg)"></div>
<div class="abs photo" role="img" aria-label="Blue card with isometric software icons illustration" style="left:180px;top:1755px;width:265px;height:350px;background:linear-gradient(160deg,#3cc2ef,#1fa6dd);transform:rotate(-8deg)"></div>

<p class="abs eyebrow" style="left:526px;top:1731px">We focuses on</p>
<h2 class="abs headline" style="left:524px;top:1768px"><strong>Software</strong> Development</h2>
<p class="abs body-copy" style="left:526px;top:1856px;width:590px">Sed ut perspiciatis unde omnis iste natus error sit voluptatem accusantium doloremque laudantium, totam rem aperiam, eaque ipsa quae ab illo inventore veritatis et quasi architecto beatae vitae dicta sunt explicabo. Nemo enim ipsam voluptatem quia voluptas sit aspernatur aut odit aut fugit, sed quia consequuntur magni dolores eos qui ratione voluptatem sequi nesciunt. Neque porro quisquam est, qui dolorem ipsum quia dolor sit amet, consectetur, adipisci velit, sed quia non numquam eius modi tempora incidunt ut labore et dolore magnam aliquam quaerat voluptatem.</p>
<div class="abs btn" style="left:526px;top:2043px;width:147px;height:42px">Read More</div>

<!-- Latest News -->
<div class="abs center" style="left:0;top:2224px;width:1200px">
  <p class="eyebrow">Read Our</p>
  <h2 class="headline" style="margin-top:6px"><strong>Latest</strong> News</h2>
</div>

<article class="abs news-card" style="left:92px;top:2366px;width:479px;height:264px">
  <p class="news-date">May 06, 2018</p>
  <h3 class="news-title">Finibus Bonorum et Malorum", written by Varelius in 45 BC</h3>
  <p class="news-text">Sed ut perspiciatis unde omnis iste natus error sit voluptatem accusantium doloremque laudantium, totam rem aperiam, eaque ipsa quae ab illo inventore veritatis et quasi architecto beatae vitae dicta sunt explicabo.</p>
  <p class="news-more">Read More</p>
</article>
<article class="abs news-card" style="left:630px;top:2366px;width:479px;height:264px">
  <p class="news-date">May 06, 2018</p>
  <h3 class="news-title">Finibus Bonorum et Malorum", written by Varelius in 45 BC</h3>
  <p class="news-text">Sed ut perspiciatis unde omnis iste natus error sit voluptatem accusantium doloremque laudantium, totam rem aperiam, eaque ipsa quae ab illo inventore veritatis et quasi architecto beatae vitae dicta sunt explicabo.</p>
  <p class="news-more">Read More</p>
</article>

<!-- Call to action -->
<p class="abs cta-kicker" style="left:111px;top:2717px">Ready to get started?</p>
<p class="abs cta-line" style="left:111px;top:2759px">Get in touch, or Free trial Products.</p>
<div class="abs btn" style="left:728px;top:2734px;width:174px;height:45px">Get a free Quote</div>
<div class="abs btn btn-dark" style="left:913px;top:2734px;width:174px;height:45px">Contact US</div>

<!-- Footer -->
<footer class="abs footer"></footer>
<div class="abs footer-brand"><span class="brand-mark"></span>Nimbra Works</div>

<div class="abs v-rule" style="left:408px;top:2937px;height:160px"></div>
<div class="abs v-rule" style="left:792px;top:2937px;height:160px"></div>

<p class="abs footer-heading" style="left:445px;top:2935px">Contact Info:</p>
<div class="abs contact-row" style="left:447px;top:2975px">
  <svg width="12" height="14" viewBox="0 0 12 14"><path d="M6 0a5 5 0 0 0-5 5c0 3.5 5 9 5 9s5-5.5 5-9a5 5 0 0 0-5-5zm0 7a2 2 0 1 1 0-4 2 2 0 0 1 0 4z" fill="#3a3a3a"/></svg>
  <div><span class="contact-name">Nimbra Works</span>42 Fenwick Lane, Marlow Bay, 40217</div>
</div>
<div class="abs contact-row" style="left:447px;top:3039px">
  <svg width="12" height="12" viewBox="0 0 12 12"><path d="M2.5 0.5l2 2.5-1.2 1.5a7 7 0 0 0 4.2 4.2L9 7.5l2.5 2-1.2 2C5 11.5 0.5 7 0.5 1.7z" fill="#3a3a3a"/></svg>
  <div>Tel: (0100) 555 0142</div>
</div>
<div class="abs contact-row" style="left:447px;top:3072px">
  <svg width="13" height="10" viewBox="0 0 13 10"><rect width="13" height="10" fill="#3a3a3a"/><path d="M0 0l6.5 5L13 0" stroke="#f3efed" stroke-width="1.2" fill="none"/></svg>
  <div>Mail: info@nimbraworks.com</div>
</div>

<p class="abs footer-heading" style="left:840px;top:2930px">Newsletter Signup</p>
<div class="abs newsletter" style="left:845px;top:2979px">
  <div class="newsletter-input">Email Address</div>
  <div class="newsletter-submit">SUBMIT</div>
</div>
<div class="abs social" style="left:841px;top:3050px">
  <span style="background:#3b5a98"></span>
  <span style="background:#2fa3e6"></span>
  <span style="background:#1b78b5"></span>
  <span style="background:#c13584"></span>
</div>

<div class="abs h-rule"></div>
<p class="abs footer-nav">Home<span>|</span>Who We Are<span>|</span>What We Do<span>|</span>Case Study<span>|</span>Blog<span>|</span>Contact Us</p>
<p class="abs copyright">Copyright © 2018. Nimbra Works. All rights reserved.</p>

</body>
</html>
```